Design a single page Shopify store web page

We are looking to have a page designed for a single page Shopify store with 2 products. We already have a basic structure that we like, though we are open to suggestions. We are looking for somebody to provide a design/color scheme that we can then implement using Shopify's templating system. We can handle the implementation(HTML / CSS / jS) as we already have 2 web developers on the team, but have not been able to find a design we liked.

The job would consist of providing a mockup (photoshop or otherwise) and any vector graphics you choose to create for the site (we can provide product photos and other images).

You can also look at http://brickwellgoods.com.au for some of our design direction we have used so far

Target Market(s)

Young Australian Males (18 - 49)

Industry/Entity Type

Store

Number of Pages Required

1 page

Font styles to use
Serif
Sans Serif

Requirements
Must have
• Single Page Design
• E-commerce Product Purchase
• Manly (whatever interpretation of that you have)

```html
<!DOCTYPE html>
<html lang="en">
<head>
<meta charset="utf-8">
<title>Brickwell — Underwear and Socks Delivered</title>
<link rel="stylesheet" href="https://fonts.googleapis.com/css2?family=Archivo+Black&family=Bebas+Neue&family=Open+Sans:wght@400;600&display=swap">
<style>
  :root {
    --ink: #111111;
    --nav-ink: #222222;
    --olive: #7b8a1b;
    --olive-step: #8c8f1f;
    --white: #ffffff;
    --sky-top: #d9dadd;
    --sky-mid: #c9cacd;
    --hill: #8f7f6c;
    --road: #5d5e60;
    --road-dark: #4a4b4d;
    --section-bg: #ececec;
    --field-bg: #050505;
    --button-bg: #e6e6e6;
    --button-ink: #333333;
    --slider-btn: #4a4d55;
    --note-tone: rgba(255,255,255,0.16);
    --note-tone-dark: rgba(17,17,17,0.08);
  }
  * { box-sizing: border-box; margin: 0; padding: 0; }
  html, body { width: 1200px; height: 1000px; overflow: hidden; }
  body { position: relative; font-family: "Open Sans", Arial, sans-serif; background: var(--section-bg); }

  .hero {
    position: absolute; left: 0; top: 0; width: 1200px; height: 735px;
    background: linear-gradient(180deg, var(--sky-top) 0%, var(--sky-mid) 38%, var(--hill) 52%, #7c7467 60%, var(--road) 72%, var(--road-dark) 100%);
  }
  .hero-photo { position: absolute; inset: 0; }

  .site-nav {
    position: absolute; left: 0; top: 63px; width: 1200px; height: 56px;
    background: var(--white);
    box-shadow: 0 4px 10px rgba(0,0,0,0.18);
    z-index: 2;
  }
  .site-nav a {
    position: absolute; top: 16px;
    font-family: "Bebas Neue", Arial, sans-serif; font-size: 25px; letter-spacing: 0.2px;
    color: var(--nav-ink); text-decoration: none; line-height: 1;
  }
  .nav-how { left: 170px; }
  .nav-plans { left: 367px; }
  .nav-faq { left: 843px; }
  .nav-about { left: 956px; }
  .brand {
    position: absolute; left: 0; width: 1200px; top: 10px; text-align: center;
    font-family: "Bebas Neue", Arial, sans-serif; font-size: 40px; color: var(--nav-ink);
    line-height: 1; letter-spacing: 1px;
  }
  .brand::before {
    content: ""; display: inline-block; width: 12px; height: 12px; background: var(--nav-ink);
    margin-right: 10px; vertical-align: 7px;
  }

  .hero-copy { position: absolute; left: 369px; top: 272px; z-index: 1; }
  .hero-kicker {
    font-family: "Archivo Black", Arial, sans-serif; font-size: 36px; color: var(--olive); line-height: 1;
  }
  .hero-title {
    font-family: "Archivo Black", Arial, sans-serif; font-size: 68px; color: var(--ink);
    line-height: 55px; margin-top: -4px; letter-spacing: 0;
    transform: scaleX(0.93); transform-origin: left top; white-space: nowrap;
  }
  .hero-sub {
    font-family: "Bebas Neue", Arial, sans-serif; font-size: 30.5px; color: var(--ink);
    line-height: 1; margin-top: 6px; letter-spacing: 0; white-space: nowrap;
  }

  .signup {
    position: absolute; left: 407px; top: 458px; width: 382px; height: 43px; display: flex;
    border-radius: 4px; overflow: hidden; box-shadow: 0 2px 4px rgba(0,0,0,0.3); z-index: 1;
  }
  .signup-field {
    width: 263px; background: var(--field-bg); color: #8a8a8a; font-size: 14px;
    padding: 14px 18px; line-height: 1;
  }
  .signup-button {
    flex: 1; background: var(--button-bg); color: var(--button-ink); font-weight: 600; font-size: 16px;
    text-align: center; padding-top: 13px; line-height: 1; letter-spacing: 0.4px;
  }

  .hand-note { position: absolute; border-radius: 8px; background: var(--note-tone); z-index: 1; }
  .note-gift { left: 180px; top: 446px; width: 228px; height: 92px; }
  .note-how { left: 500px; top: 506px; width: 142px; height: 100px; }

  .slider-btn {
    position: absolute; top: 412px; width: 30px; height: 30px; border-radius: 50%;
    background: var(--slider-btn); z-index: 1;
  }
  .slider-prev { left: 100px; }
  .slider-next { left: 1042px; }
  .slider-btn svg { position: absolute; left: 0; top: 0; }

  .how-it-works { position: absolute; left: 0; top: 735px; width: 1200px; height: 265px; }
  .how-title {
    position: absolute; top: 62px; width: 1200px; text-align: center;
    font-family: "Bebas Neue", Arial, sans-serif; font-size: 52px; color: var(--ink); line-height: 1;
  }
  .step {
    position: absolute; top: 173px; width: 236px; height: 236px; border-radius: 50%;
    background: var(--white); box-shadow: 0 0 8px rgba(0,0,0,0.2);
    text-align: center; padding-top: 60px;
    font-family: "Bebas Neue", Arial, sans-serif; font-size: 36px; line-height: 0.85; color: var(--ink);
  }
  .step span { color: var(--olive-step); }
  .step-plan { left: 172px; }
  .step-often { left: 482px; }
  .step-pack { left: 792px; }
  .step-arrow {
    position: absolute; left: 682px; top: 155px; width: 144px; height: 72px;
    border-radius: 8px; background: var(--note-tone-dark);
  }
</style>
</head>
<body>
  <section class="hero">
    <div class="hero-photo" role="img" aria-label="Photograph of an empty mountain road stretching through a misty valley"></div>

    <nav class="site-nav">
      <a class="nav-how" href="#how">How it works</a>
      <a class="nav-plans" href="#plans">Plans</a>
      <div class="brand">BRICKWELL</div>
      <a class="nav-faq" href="#faq">FAQ</a>
      <a class="nav-about" href="#about">About us</a>
    </nav>

    <div class="hero-copy">
      <div class="hero-kicker">NEW</div>
      <h1 class="hero-title">UNDERWEAR<br>AND SOCKS</h1>
      <p class="hero-sub">Delivered to your door · Every 3 or 6 months</p>
    </div>

    <form class="signup">
      <div class="signup-field">enter your email address</div>
      <div class="signup-button">subscribe</div>
    </form>

    <div class="hand-note note-gift" role="img" aria-label="Hand-lettered note with a curved arrow offering a free gift with the first pack"></div>
    <div class="hand-note note-how" role="img" aria-label="Hand-lettered note with a downward arrow inviting visitors to see how it works"></div>

    <div class="slider-btn slider-prev"><svg width="30" height="30" viewBox="0 0 30 30"><path d="M17.5 9 L11.5 15 L17.5 21" stroke="#fff" stroke-width="3" fill="none"/></svg></div>
    <div class="slider-btn slider-next"><svg width="30" height="30" viewBox="0 0 30 30"><path d="M12.5 9 L18.5 15 L12.5 21" stroke="#fff" stroke-width="3" fill="none"/></svg></div>
  </section>

  <section class="how-it-works" id="how">
    <h2 class="how-title">HOW IT WORKS</h2>
    <div class="step step-plan"><span>1.</span> CHOOSE<br>A PLAN</div>
    <div class="step step-often"><span>2.</span> CHOOSE<br>HOW OFTEN</div>
    <div class="step step-pack"><span>3.</span> GET YOUR<br>PACK</div>
    <div class="step-arrow" role="img" aria-label="Brush-drawn arrow pointing from step two to step three"></div>
  </section>
</body>
</html>
```